Website for Brisbeck Current Glide

Require a website for a river float in the City of Edmonton. Located on North Saskatchewan River. Will need to be a coded website with incorporated booking system through Fare Harbor software.

Pages include
Home
Pricing
About
FAQ
Contact

Brisbeck Current Glide is an activity based business that will have customers floating down the North Saskatchewan river in Edmonton AB. The site will have all information needed and a full reservation system. The project was launched to provide people in the Edmonton area a favorite summer activity.

Here are similar websites to reference what our business will be doing and what we are looking for.

mellowbendcanoehire.example
pinegulchloopers.example

Target Market(s)

Families, Groups, Individuals, Anyone who wants to explore the river

Industry/Entity Type

Activities based business/ Outdoor recreational/ River Float

Coding

Coded - Design and coding required

Number of Pages Required

5+ page

Colors
0054AA
0677BA
7BADD7
CADEEF
E8F1F8
F0912C
F2A743
F7CA91
FBE8D2
FDF5EE

```html
<!DOCTYPE html>
<html lang="en">
<head>
<meta charset="utf-8">
<title>Brisbeck Current Glide</title>
<link rel="stylesheet" href="https://fonts.googleapis.com/css2?family=Raleway:wght@400;700;800&family=Mulish:wght@400;600;700&family=Oswald:wght@300;400&display=swap">
<style>
:root{
  --blue-deep:#0054AA;
  --blue:#0677BA;
  --blue-soft:#7BADD7;
  --blue-pale:#CADEEF;
  --aqua:#4FC6E6;
  --orange:#F0912C;
  --orange-light:#F2A743;
  --navy:#062640;
  --ink:#2b2b2b;
  --white:#ffffff;
  --line:#9a9a9a;
}
*{margin:0;padding:0;box-sizing:border-box}
html,body{width:1200px;height:2496px;overflow:hidden}
body{position:relative;background:var(--white);font-family:"Mulish",sans-serif;color:var(--ink)}
.abs{position:absolute}
.btn{position:absolute;display:flex;align-items:center;justify-content:center;background:var(--orange);color:var(--white);font:600 12px "Mulish",sans-serif;letter-spacing:.3px;text-transform:uppercase}

/* hero */
.hero{position:absolute;left:0;top:0;width:1200px;height:600px;overflow:hidden}
.hero-photo{position:absolute;inset:0;background:
  linear-gradient(180deg,#9aa4b4 0%,#8a95a4 25%,#6f7a77 45%,#4f6a3e 62%,#6b7f86 78%,#56707a 100%)}
.hero-wave{position:absolute;left:0;top:0}
.topbar{position:absolute;top:12px;left:0;width:1200px;height:16px}
.topbar .call{position:absolute;left:829px;top:0;font:600 10px "Mulish",sans-serif;color:var(--white)}
.social-dot{position:absolute;top:2px;width:12px;height:12px;border-radius:50%;background:rgba(255,255,255,.85)}
.brand-top{position:absolute;left:130px;top:48px;display:flex;align-items:center;gap:6px}
.brand-top .dot{width:14px;height:14px;border-radius:50%;background:var(--aqua)}
.brand-top span{font:700 12px "Raleway",sans-serif;color:var(--white)}
.nav{position:absolute;top:49px;left:676px;display:flex;gap:0}
.nav a{font:600 11.5px "Mulish",sans-serif;color:var(--white);text-decoration:none;position:absolute;white-space:nowrap}
.nav a.active::after{content:"";position:absolute;left:0;right:0;bottom:-6px;height:2px;background:var(--orange)}
.hero-title{position:absolute;left:680px;top:194px;color:var(--white);font-family:"Raleway",sans-serif;font-weight:800;line-height:1}
.hero-title .l1{display:block;font-size:33px}
.hero-title .l2{display:block;font-size:46px;margin-top:4px}
.hero-sub{position:absolute;left:681px;top:292px;font:400 13.5px "Mulish",sans-serif;color:var(--white)}

.ring{position:absolute;border-radius:50%;border-style:solid;border-color:var(--aqua)}

/* gear */
.gear-head{position:absolute;top:625px;left:0;width:1200px;text-align:center}
.gear-head .t1{font:400 32px "Raleway",sans-serif;color:var(--ink)}
.gear-head .t2{font:800 32px "Raleway",sans-serif;color:var(--ink);margin-top:2px}
.gear-head p{font:400 13.5px "Mulish",sans-serif;margin-top:12px}
.card{position:absolute;top:756px;width:220px;height:253px;background:var(--blue);border-radius:110px 110px 0 0}
.card-photo{position:absolute;left:17px;top:20px;width:186px;height:140px;border-radius:93px 93px 0 0;overflow:hidden}
.card-photo svg{position:absolute;left:0;bottom:0}
.card-label{position:absolute;left:0;right:0;top:196px;text-align:center;font:400 22px "Oswald",sans-serif;color:var(--white);transform:scaleX(.82)}

/* band */
.band{position:absolute;left:0;top:1158px;width:1200px;height:456px;overflow:hidden;
  background:linear-gradient(90deg,#3c4c4a 0%,#55615f 30%,#5b5d5c 50%,#46524e 70%,#2f3d3c 100%)}
.band::after{content:"";position:absolute;inset:0;background:rgba(30,45,55,.45)}
.band-text{position:absolute;left:0;top:1254px;width:1200px;text-align:center;color:var(--white);z-index:2}
.band-text h2{font:800 33px "Raleway",sans-serif}
.band-text p{font:400 13.5px/20px "Mulish",sans-serif;margin-top:21px}

/* contact */
.brand-big{position:absolute;left:131px;top:1681px;width:358px;height:310px;display:flex;flex-direction:column;align-items:center;justify-content:center;gap:22px}
.brand-big .badge{width:200px;height:200px;border-radius:50%;background:var(--aqua)}
.brand-big span{font:800 34px "Raleway",sans-serif;color:var(--navy);text-align:center;line-height:1.1}
.contact-title{position:absolute;left:543px;top:1728px;font:800 32px "Raleway",sans-serif;color:var(--ink)}
.contact-sub{position:absolute;left:543px;top:1769px;font:400 13.5px "Mulish",sans-serif}
.field{position:absolute;border:1px solid var(--line);font:400 10px "Mulish",sans-serif;color:var(--ink);padding:12px 16px}

/* footer */
.foot-arc{position:absolute;left:0;top:0}
.news-title{position:absolute;top:2110px;left:0;width:1200px;text-align:center;font:800 32px "Raleway",sans-serif;color:var(--white)}
.news-input{position:absolute;left:349px;top:2186px;width:502px;height:30px;border-bottom:1px solid #5a7890;font:400 10px "Mulish",sans-serif;color:var(--white);padding-top:13px}
.info{position:absolute;top:2278px;display:flex;align-items:center;gap:8px;font:400 11.5px "Mulish",sans-serif;color:var(--white)}
.info .ico{width:30px;height:30px;border:1.5px solid var(--aqua);border-radius:50%;display:flex;align-items:center;justify-content:center}
.foot-rule{position:absolute;left:131px;top:2345px;width:938px;height:1px;background:#21415a}
.foot-links{position:absolute;top:2381px;left:0;width:1200px;text-align:center;font:600 10px "Mulish",sans-serif;color:var(--white);word-spacing:4px}
.copy{position:absolute;top:2404px;left:0;width:1200px;text-align:center;font:400 8.5px "Mulish",sans-serif;color:#4f6a80}
.copy b{font-weight:400;color:#9fb4c6}
.social{position:absolute;top:2435px;width:35px;height:35px;border-radius:50%;border:1.5px solid var(--white)}
.social.solid{background:#1877d6;border-color:#1877d6}
</style>
</head>
<body>

<header class="hero">
  <div class="hero-photo" role="img" aria-label="Edmonton downtown skyline above the river valley with a bridge and trees, tinted photo"></div>
  <svg class="hero-wave" width="1200" height="600" viewBox="0 0 1200 600">
    <path d="M0,520 C120,575 250,535 380,575 C460,598 560,585 640,548 C705,518 720,462 800,440 C900,412 1000,392 1080,410 C1140,425 1165,462 1200,440 L1200,600 L0,600 Z" fill="#fff"/>
    <path d="M0,520 C120,575 250,535 380,575 C460,598 560,585 640,548 C705,518 720,462 800,440 C900,412 1000,392 1080,410 C1140,425 1165,462 1200,440" fill="none" stroke="#4FC6E6" stroke-width="16"/>
  </svg>
  <div class="topbar">
    <span class="call">Call Us: +1 (780) 555 0147</span>
    <span class="social-dot" style="left:992px"></span>
    <span class="social-dot" style="left:1023px"></span>
    <span class="social-dot" style="left:1056px"></span>
  </div>
  <div class="brand-top"><i class="dot"></i><span>Brisbeck Current Glide</span></div>
  <nav class="nav">
    <a class="active" style="left:0">HOME</a>
    <a style="left:85px">PRICING</a>
    <a style="left:181px">ABOUT</a>
    <a style="left:270px">FAQ</a>
    <a style="left:343px">CONTACT</a>
  </nav>
  <h1 class="hero-title"><span class="l1">BRISBECK</span><span class="l2">CURRENT GLIDE</span></h1>
  <p class="hero-sub">Float the North Saskatchewan through downtown Edmonton</p>
  <a class="btn" style="left:682px;top:330px;width:123px;height:38px">Book now</a>
</header>

<span class="ring" style="left:924px;top:431px;width:40px;height:40px;border-width:6px"></span>
<span class="ring" style="left:983px;top:461px;width:19px;height:19px;border-width:4px"></span>
<span class="ring" style="left:52px;top:565px;width:20px;height:20px;border-width:4px"></span>
<span class="ring" style="left:91px;top:575px;width:40px;height:40px;border-width:6px"></span>

<section>
  <div class="gear-head">
    <div class="t1">SHUTTLE</div>
    <div class="t2">SERVICE AND GEAR INCLUDED</div>
    <p>We provide everything you need including</p>
  </div>

  <div class="card" style="left:130px">
    <div class="card-photo" role="img" aria-label="Orange camper van with boards on the roof" style="background:linear-gradient(180deg,#cfe3ef,#e9a35a 60%,#6d7b83)"></div>
    <div class="card-label">Round Trip Shuttle Service</div>
  </div>
  <div class="card" style="left:370px">
    <div class="card-photo" role="img" aria-label="Inflatable float tubes on the water" style="background:linear-gradient(160deg,#4fb0a8,#e7c7bb 55%,#b9a48e)"></div>
    <div class="card-label">Float Tube</div>
  </div>
  <div class="card" style="left:610px">
    <div class="card-photo" role="img" aria-label="Lifejackets hanging on a rack" style="background:linear-gradient(180deg,#dfe3e6,#d6552c 50%,#2a3a5a)"></div>
    <div class="card-label">Lifejacket</div>
  </div>
  <div class="card" style="left:850px">
    <div class="card-photo" role="img" aria-label="Paddler standing on a board on a calm lake" style="background:linear-gradient(180deg,#c7d6e2,#8fa9bd 55%,#d9c58a)"></div>
    <div class="card-label">Paddle</div>
  </div>

  <a class="btn" style="left:539px;top:1061px;width:123px;height:37px">Read more</a>
</section>

<section>
  <div class="band" role="img" aria-label="Group of friends in swimwear relaxing by the river, darkened photo"></div>
  <svg class="abs" style="left:0;top:1150px" width="1200" height="40" viewBox="0 0 1200 40">
    <path d="M0,0 L1200,0 L1200,18 L1150,22 L1100,15 L1040,24 L980,16 L930,21 L870,14 L800,22 L740,17 L680,24 L620,15 L560,22 L500,16 L440,23 L380,12 L330,20 L270,16 L210,23 L150,15 L90,21 L40,17 L0,24 Z" fill="#fff"/>
  </svg>
  <div class="band-text">
    <h2>FLOATING 7 &amp; DAYS A WEEK</h2>
    <p>Our priority is to make sure everyone has a safe and fun time on the river. Safety demonstrations are provided and staff<br>are available to assist in any way. Whether you are a family with children, larger group or just want a relaxing way to explore the river,<br>this is a must try activity.</p>
  </div>
  <a class="btn" style="left:539px;top:1407px;width:123px;height:37px;z-index:2">Book now</a>
  <span class="ring" style="left:989px;top:1144px;width:40px;height:40px;border-width:6px;z-index:2"></span>
  <span class="ring" style="left:1049px;top:1175px;width:19px;height:19px;border-width:4px;z-index:2"></span>
  <span class="ring" style="left:131px;top:1584px;width:20px;height:20px;border-width:4px;z-index:2"></span>
  <span class="ring" style="left:170px;top:1594px;width:40px;height:40px;border-width:6px;z-index:2"></span>
</section>

<section>
  <div class="brand-big"><i class="badge"></i><span>Brisbeck<br>Current Glide</span></div>
  <h2 class="contact-title">CONTACT US</h2>
  <p class="contact-sub">We’d love to hear from you!</p>
  <div class="field" style="left:543px;top:1807px;width:260px;height:36px">Name:</div>
  <div class="field" style="left:543px;top:1854px;width:260px;height:36px">Email:</div>
  <div class="field" style="left:543px;top:1901px;width:260px;height:36px">Phone:</div>
  <div class="field" style="left:810px;top:1807px;width:260px;height:84px">Message:</div>
  <a class="btn" style="left:810px;top:1901px;width:260px;height:36px;font-size:10.5px">Submit</a>
</section>

<footer>
  <svg class="foot-arc" width="1200" height="2496" viewBox="0 0 1200 2496">
    <path d="M0,2496 C10,2230 300,2046 600,2046 C900,2046 1190,2230 1200,2496 Z" fill="#062640"/>
  </svg>
  <span class="ring" style="left:269px;top:2083px;width:20px;height:20px;border-width:4px"></span>
  <span class="ring" style="left:308px;top:2093px;width:40px;height:40px;border-width:6px"></span>
  <span class="ring" style="left:1074px;top:2279px;width:40px;height:40px;border-width:6px"></span>
  <span class="ring" style="left:1134px;top:2310px;width:19px;height:19px;border-width:4px"></span>

  <h2 class="news-title">NEWSLETTER</h2>
  <div class="news-input">Enter Your Email:</div>
  <a class="btn" style="left:760px;top:2178px;width:91px;height:32px;text-transform:none;font-weight:400;font-size:10.5px">Subscribe</a>

  <div class="info" style="left:190px">
    <span class="ico"><svg width="12" height="14" viewBox="0 0 12 14"><path d="M6,0 C2.7,0 0.5,2.4 0.5,5.3 C0.5,9 6,14 6,14 C6,14 11.5,9 11.5,5.3 C11.5,2.4 9.3,0 6,0 Z" fill="#fff"/><circle cx="6" cy="5.3" r="2" fill="#062640"/></svg></span>
    4120 Ferrow Bend Rd, Edmonton, AB
  </div>
  <div class="info" style="left:533px">
    <span class="ico"><svg width="12" height="12" viewBox="0 0 12 12"><path d="M2.6,0.6 L4.4,2.9 L3.3,4.3 C4,5.9 6.1,8 7.7,8.7 L9.1,7.6 L11.4,9.4 L10.3,11.3 C5.6,11.4 0.6,6.4 0.7,1.7 Z" fill="#fff"/></svg></span>
    +1 (780) 555 0147
  </div>
  <div class="info" style="left:799px">
    <span class="ico"><svg width="13" height="10" viewBox="0 0 13 10"><rect x="0.5" y="0.5" width="12" height="9" fill="#fff"/><path d="M0.5,0.8 L6.5,5.5 L12.5,0.8" fill="none" stroke="#062640" stroke-width="1.2"/></svg></span>
    hello@brisbeckglide.example
  </div>

  <div class="foot-rule"></div>
  <nav class="foot-links">HOME &nbsp;| &nbsp;PRICING &nbsp;| &nbsp;ABOUT &nbsp;| &nbsp;FAQ &nbsp;| &nbsp;CONTACT</nav>
  <p class="copy">COPYRIGHT © 2022 <b>BRISBECK CURRENT GLIDE</b>. ALL RIGHTS RESERVED.</p>
  <span class="social solid" style="left:535px"></span>
  <span class="social" style="left:582px"></span>
  <span class="social" style="left:630px"></span>
</footer>

</body>
</html>
```